Marrowgate Auctions Business Cards Design Needed

I need a business card design that is modern looking - double sided (maybe just my logo on the back, but open to suggestions) - the overall design is up to you. I want it to be easy to read - not over the top flashy. I already have a company logo which I uploaded so that needs to be used. The colors of my logo are the colors I want on the card... so blue and gray (do need to match the logo colors).

Requirements
Must have
• Would like the card to be sleek, modern and easy to ready

```html
<!DOCTYPE html>
<html lang="en">
<head>
<meta charset="utf-8">
<title>Marrowgate Auctions – Business Cards</title>
<link rel="stylesheet" href="https://fonts.googleapis.com/css2?family=Open+Sans:wght@400;600;700&display=swap">
<style>
  :root {
    --backdrop: #3b332e;
    --card: #1e2124;
    --card-edge: #2a2d31;
    --brand-blue: #2f7fc8;
    --brand-gray: #8d9297;
    --silver: #c9cdd1;
    --text-light: #f1f2f3;
    --rule: #6f747a;
  }
  * { box-sizing: border-box; margin: 0; padding: 0; }
  html, body {
    width: 1200px; height: 864px; overflow: hidden;
    background: var(--backdrop);
    font-family: "Open Sans", Arial, sans-serif;
  }
  .canvas { position: relative; width: 1200px; height: 864px; }
  .card {
    position: absolute; width: 520px; height: 298px;
    background: var(--card);
    border: 1px solid var(--card-edge);
    box-shadow: 0 14px 30px rgba(0,0,0,.45);
  }
  /* Back side */
  .card--back { left: 50px; top: 120px; }
  .back__brand {
    position: absolute; left: 0; right: 0; top: 96px;
    text-align: center; color: var(--silver);
    font-weight: 700; font-size: 40px; letter-spacing: 1px;
  }
  .back__tagline {
    position: absolute; left: 40px; bottom: 56px;
    color: var(--text-light); font-size: 14px;
  }
  /* Front side */
  .card--front { left: 630px; top: 440px; }
  .front__name {
    position: absolute; left: 32px; top: 54px;
    color: var(--brand-blue); font-weight: 700; font-size: 21px; letter-spacing: .5px;
  }
  .front__title {
    position: absolute; left: 32px; top: 84px;
    color: var(--text-light); font-weight: 600; font-size: 14px;
  }
  .front__rule-short {
    position: absolute; left: 32px; top: 110px; width: 240px; height: 1px; background: var(--rule);
  }
  .front__contacts { position: absolute; left: 32px; top: 120px; list-style: none; }
  .front__contacts li {
    display: flex; align-items: center; gap: 8px;
    color: var(--text-light); font-size: 14px; line-height: 22px;
  }
  .front__contacts svg { width: 12px; height: 12px; fill: var(--brand-blue); flex: none; }
  .front__brand {
    position: absolute; right: 30px; top: 48px; width: 170px;
    text-align: right; line-height: 1.15;
    color: var(--brand-blue); font-weight: 700; font-size: 24px;
  }
  .front__rule-long {
    position: absolute; left: 32px; right: 30px; bottom: 70px; height: 1px; background: var(--rule);
  }
</style>
</head>
<body>
<main class="canvas">
  <section class="card card--back" aria-label="Card back">
    <div class="back__brand">Marrowgate</div>
    <p class="back__tagline">Improving Charity Auctions Nationwide</p>
  </section>

  <section class="card card--front" aria-label="Card front">
    <h1 class="front__name">OWEN HARLOW</h1>
    <p class="front__title">Owner/President - Auctioneer</p>
    <div class="front__rule-short"></div>
    <ul class="front__contacts">
      <li><svg viewBox="0 0 24 24"><path d="M6.6 10.8a15.5 15.5 0 0 0 6.6 6.6l2.2-2.2c.3-.3.7-.4 1-.2 1.1.4 2.3.6 3.6.6.6 0 1 .4 1 1V20c0 .6-.4 1-1 1C10.6 21 3 13.4 3 4c0-.6.4-1 1-1h3.5c.6 0 1 .4 1 1 0 1.3.2 2.5.6 3.6.1.3 0 .7-.2 1z"/></svg>702-555-0148</li>
      <li><svg viewBox="0 0 24 24"><path d="M2 5h20v14H2zM4 7v.5l8 5 8-5V7l-8 5z"/></svg>harlowbids@mailbox.com</li>
      <li><svg viewBox="0 0 24 24"><circle cx="12" cy="12" r="10"/></svg>www.gavelrescue.com</li>
    </ul>
    <div class="front__brand">Marrowgate<br>Auctions</div>
    <div class="front__rule-long"></div>
  </section>
</main>
</body>
</html>
```